Flyer-Design für Aktionstag einer Mondtal-Station gesucht
Zielgruppe
Ursprünglich ist die Mondtalstation eine Idee aus Schweden, doch inzwischen haben Fach-schaften in Deutschland an vielen medizinischen Universitäten diese Idee aufgenommen und umgesetzt. Seit einigen Jahren gibt es die Mondtalstation auch an der Universität zu Wendhagen, als AG der Fachschaft Medizin.
Aufgabenstellung
siehe Briefing-Dokument

```html
<!DOCTYPE html>
<html lang="de">
<head>
<meta charset="utf-8">
<title>Mondtalstation – Aktionstag Flyer</title>
<link href="https://fonts.googleapis.com/css2?family=Fira+Sans:wght@500;600&family=Noto+Serif:wght@400&display=swap" rel="stylesheet">
<style>
  :root {
    --stage: #cdeee6;
    --paper: #f4f4f5;
    --photo-light: #f1f1f3;
    --photo-mid: #e4e4e8;
    --ink: #143833;
    --ink-soft: #1d4540;
    --white: #ffffff;
  }
  * { margin: 0; padding: 0; box-sizing: border-box; }
  html, body {
    width: 1200px; height: 900px; overflow: hidden;
    background: var(--stage);
  }
  .flyer {
    position: absolute; left: 400px; top: 25px;
    width: 400px; height: 850px;
    background: var(--paper);
    overflow: hidden;
    font-family: "Fira Sans", sans-serif;
    color: var(--ink);
  }
  .hero-photo {
    position: absolute; left: 0; top: 0; width: 400px; height: 760px;
    background: linear-gradient(180deg, var(--photo-light) 0%, var(--photo-mid) 100%);
  }
  .hero-photo .subject {
    position: absolute; left: 70px; top: 150px; width: 230px; height: 600px;
    background: radial-gradient(ellipse at 50% 40%, #dcdce2 0%, #d4d6de 45%, rgba(228,228,232,0) 75%);
  }
  .tagline {
    position: absolute; right: 34px; top: 70px;
    text-align: right; font-weight: 600; font-size: 22px; line-height: 27px;
    letter-spacing: 0.5px; text-transform: uppercase;
  }
  .tagline .highlight {
    background: var(--ink); color: var(--white); padding: 0 6px;
  }
  .teddy-icon {
    position: absolute; left: 40px; top: 395px; width: 46px; height: 48px;
    border-radius: 8px;
    background: linear-gradient(160deg, #a8805b, #7a583c);
  }
  .title-band {
    position: absolute; left: 0; top: 440px; width: 380px;
    background: var(--ink); color: var(--white);
    padding: 10px 16px 10px 20px;
    text-align: right; text-transform: uppercase;
    font-weight: 600; font-size: 25px; line-height: 30px; letter-spacing: 0.6px;
  }
  .intro {
    position: absolute; left: 40px; top: 530px; width: 320px;
    font-family: "Noto Serif", serif; font-size: 12.5px; line-height: 17px;
    color: var(--ink);
  }
  .event-details {
    position: absolute; left: 40px; top: 650px;
    text-transform: uppercase; font-weight: 600; font-size: 18px; line-height: 24px;
    letter-spacing: 0.6px;
  }
  .event-details .boxed {
    display: inline-block; background: var(--ink); color: var(--white);
    padding: 0 8px; margin-bottom: 2px;
  }
  .event-details .place { color: var(--ink); padding-left: 2px; }
  .footer {
    position: absolute; left: 0; bottom: 0; width: 400px; height: 90px;
    display: flex; align-items: center; justify-content: center; gap: 12px;
    background: var(--paper);
  }
  .footer .mark {
    width: 36px; height: 36px; border-radius: 50%;
    border: 1.5px solid var(--ink-soft);
  }
  .footer .org-name {
    font-weight: 500; font-size: 10px; letter-spacing: 2px;
    text-transform: uppercase; color: var(--ink-soft);
  }
</style>
</head>
<body>
  <main class="flyer">
    <div class="hero-photo">
      <div class="subject" role="img" aria-label="Foto: Kind im Arztkittel mit Stethoskop untersucht einen verbundenen Teddybären"></div>
    </div>

    <h2 class="tagline">
      Der <span class="highlight">kostenlose</span><br>
      Gesundheitscheck<br>
      für Teddy
    </h2>

    <div class="teddy-icon" role="img" aria-label="Illustration: kleiner Teddybär mit Stethoskop"></div>

    <h1 class="title-band">Mondtalstation an der<br>Universität zu Wendhagen</h1>

    <p class="intro">
      Am Aktionstag werden wir die Lieblingsstofftiere der Kinder „behandeln“ und die Kinder als Teddy-Eltern in alle Abläufe einbeziehen.
    </p>

    <div class="event-details">
      <span class="boxed">22. Juni 2019</span><br>
      <span class="boxed">10:00 bis 16:00 Uhr</span><br>
      <span class="place">Platz am Rathaus.</span>
    </div>

    <footer class="footer">
      <span class="mark"></span>
      <span class="org-name">Universität zu Wendhagen</span>
    </footer>
  </main>
</body>
</html>
```